Online-Marketing Material für Immobilienmakler
Zielgruppe
Ich bin Immobilienmakler und beschäftige mich mit der Vermietung / Verkauf von Immobilien. Zielgruppe sind Käufer / Verkäufer bzw. Vermieter und Mieter
Aufgabenstellung
Das Design soll sich am bestehenden CI orientieren, gleichzeitig modern gestaltet werden. Hierbei geht es mir um die Erstellung von Desginvorlagen für Post in Social-Media-Kanälen, welche ich je nach Inhalt entsprechend anpassen kann.
Inbesondere soll es eine Vorlage für die Vorstellung von neuen Objekten geben, welche immer wieder genutzt werden kann und daher die Inhalte in Canva anpassbar sind.

```html
<!DOCTYPE html>
<html lang="de">
<head>
<meta charset="utf-8">
<title>klarwohn.immo – Objektvorstellung</title>
<link rel="stylesheet" href="https://fonts.googleapis.com/css2?family=Red+Hat+Display:wght@400;500;700;800;900&display=swap">
<style>
  :root {
    --brand-blue: #0583c4;
    --brand-blue-dark: #0a6fa6;
    --brand-green: #7fbf42;
    --white: #ffffff;
    --stage: #6b6b6b;
    --photo-sky: #c2b8ae;
    --photo-mid: #59684a;
    --photo-low: #2e3b29;
  }
  html, body {
    margin: 0;
    width: 1200px;
    height: 1117px;
    overflow: hidden;
    background: var(--stage);
    font-family: "Red Hat Display", sans-serif;
  }
  .flyer {
    position: absolute;
    left: 70px;
    top: 28px;
    width: 1430px;
    height: 1430px;
    transform: scale(0.7413);
    transform-origin: top left;
    background: var(--white);
    overflow: hidden;
  }
  .flyer-shapes {
    position: absolute;
    inset: 0;
  }
  .brand-name {
    position: absolute;
    left: 107px;
    top: 72px;
    margin: 0;
    font-weight: 800;
    font-size: 84px;
    line-height: 1.1;
    letter-spacing: -1px;
    color: var(--brand-blue);
  }
  .headline {
    position: absolute;
    left: 0;
    right: 0;
    top: 692px;
    margin: 0;
    text-align: center;
    font-weight: 800;
    font-size: 74px;
    letter-spacing: 0.5px;
    color: var(--white);
  }
  .features {
    position: absolute;
    left: 60px;
    width: 1310px;
    top: 875px;
    height: 337px;
    display: flex;
  }
  .feature {
    flex: 1;
    display: flex;
    flex-direction: column;
    align-items: center;
    padding-top: 17px;
  }
  .feature + .feature { border-left: 4px solid var(--brand-blue-dark); }
  .feature-mark {
    width: 92px;
    height: 92px;
    background: var(--brand-green);
    margin-bottom: 32px;
  }
  .feature-text {
    margin: 0;
    width: 340px;
    text-align: center;
    font-weight: 500;
    font-size: 32px;
    line-height: 37px;
    color: var(--white);
  }
  .contact-bar {
    position: absolute;
    left: 160px;
    top: 1280px;
    width: 1120px;
    height: 50px;
    display: flex;
    align-items: center;
    justify-content: center;
    font-weight: 500;
    font-size: 30px;
    color: var(--white);
  }
  .contact-item {
    display: flex;
    align-items: center;
    gap: 14px;
    padding: 0 18px;
  }
  .contact-item + .contact-item { border-left: 2px solid rgba(255,255,255,0.5); }
  .contact-icon { width: 34px; height: 34px; }
</style>
</head>
<body>
<main class="flyer">
  <svg class="flyer-shapes" viewBox="0 0 1430 1430" width="1430" height="1430">
    <defs>
      <linearGradient id="photoTones" x1="0" y1="0" x2="0" y2="1">
        <stop offset="0" stop-color="var(--photo-sky)"/>
        <stop offset="0.45" stop-color="#9a958c"/>
        <stop offset="0.75" stop-color="var(--photo-mid)"/>
        <stop offset="1" stop-color="var(--photo-low)"/>
      </linearGradient>
    </defs>
    <polygon class="property-photo" role="img" aria-label="Foto: modernes Einfamilienhaus mit Solardach und beleuchteten Fenstern in der Abenddämmerung, umgeben von Bäumen"
             points="0,225 695,225 828,74 1430,74 1430,827 0,827" fill="url(#photoTones)"/>
    <rect class="accent-band-blue" x="0" y="225" width="390" height="60" fill="var(--brand-blue)"/>
    <polygon class="accent-band-green" points="828,74 1298,74 1245,135 775,135" fill="var(--brand-green)"/>
    <rect class="info-panel" x="0" y="827" width="1430" height="603" fill="var(--brand-blue)"/>
    <polygon class="contact-bar-shadow" points="102,1350 1310,1350 1345,1274 1335,1274 1300,1342 95,1342" fill="var(--brand-blue-dark)"/>
    <polygon class="contact-bar-shape" points="130,1267 1335,1267 1300,1342 95,1342" fill="var(--brand-green)"/>
  </svg>

  <p class="brand-name">klarwohn.immo</p>

  <h1 class="headline">NEUBAU-ETWS IN BERNLOCH</h1>

  <section class="features">
    <div class="feature">
      <span class="feature-mark"></span>
      <p class="feature-text">Lorem ipsum dolor sit amet, consectetuer adipiscing elit, sed nonummy nibh euis tincidunt ut laoreet.</p>
    </div>
    <div class="feature">
      <span class="feature-mark"></span>
      <p class="feature-text">Lorem ipsum dolor sit amet, consectetuer adipiscing elit, sed nonummy nibh euis tincidunt ut laoreet.</p>
    </div>
    <div class="feature">
      <span class="feature-mark"></span>
      <p class="feature-text">Lorem ipsum dolor sit amet, consectetuer adipiscing elit, sed nonummy nibh euis tincidunt ut laoreet.</p>
    </div>
  </section>

  <div class="contact-bar">
    <span class="contact-item">
      <svg class="contact-icon" viewBox="0 0 24 24"><circle cx="12" cy="12" r="11" fill="var(--white)"/><path d="M8.2 6.5l2 2.3-1.2 1.4c.8 1.7 2 2.9 3.7 3.7l1.4-1.2 2.3 2-1.3 1.8c-4 -.5-7.6-4.1-8.1-8.1z" fill="var(--brand-green)"/></svg>
      0 7345 / 210 4560
    </span>
    <span class="contact-item">
      <svg class="contact-icon" viewBox="0 0 24 24" fill="none" stroke="var(--white)" stroke-width="1.6"><rect x="2.5" y="5.5" width="19" height="13"/><path d="M2.5 5.5l9.5 7.5 9.5-7.5M2.5 18.5l7-6M21.5 18.5l-7-6"/></svg>
      info@klarwohn.immo
    </span>
    <span class="contact-item">
      <svg class="contact-icon" viewBox="0 0 24 24" fill="none" stroke="var(--white)" stroke-width="1.5"><circle cx="12" cy="12" r="10"/><ellipse cx="12" cy="12" rx="4.5" ry="10"/><path d="M2 12h20M4 7h16M4 17h16"/></svg>
      www.klarwohn.immo
    </span>
  </div>
</main>
</body>
</html>
```